Inviting A6 Flyer for Church membership

We need an A6 size flyer for the church. We are looking for something fresh, inviting and impactful. Church new logo and current flyer design attached.
Back text as follows:
We would love to have you join us as our SPECIAL GUEST this Sunday at 10am.
You can find us at Harvest Lantern Family Church, 17-19 Marlow Crest Road
(Behind Brivo), Thornbury Meadow Village,QX4 7LB
For more information or for a chat, please call us on 07700 900418 / 07700 900752 or email church@hlfcuk-mail.test
Target Market(s)
Church
Industry/Entity Type
Church
Colors
Designer to choose colors to be used in the design.
Requirements
Must have
- fresh, inviting and impactful.
- Chruch logo (attached)
Should not have
- Too much going on

```html
<!DOCTYPE html>
<html lang="en">
<head>
<meta charset="utf-8">
<title>Harvest Lantern Family Church – Welcome Flyer</title>
<link rel="stylesheet" href="https://fonts.googleapis.com/css2?family=Bodoni+Moda:wght@400&family=Federo&family=Comfortaa:wght@300;400;500&family=Encode+Sans+Condensed:wght@400&display=swap">
<style>
  :root {
    --backdrop: #d4d4d4;
    --sky-top: #cfe3f6;
    --sky-mid: #bccdd6;
    --haze: #a9b7b4;
    --forest: #4d5a2f;
    --forest-dark: #2c3421;
    --road: #45494b;
    --welcome-green: #37b24d;
    --flourish-green: #8ccf3f;
    --ink: #1d1f22;
    --guest-red: #e8202a;
    --paper: #ffffff;
    --edge-blue: #1f6fc0;
    --logo-red: #c1272d;
  }
  html, body {
    margin: 0;
    width: 1200px;
    height: 1200px;
    overflow: hidden;
    background: var(--backdrop);
  }
  .flyer-card {
    position: absolute;
    overflow: hidden;
  }
  .flyer-front { left: 234px; top: 66px; width: 718px; height: 516px; }
  .flyer-back  { left: 230px; top: 617px; width: 728px; height: 527px; }

  .scenery {
    position: absolute;
    inset: 0;
    background: linear-gradient(180deg,
      var(--sky-top) 0%,
      var(--sky-mid) 42%,
      var(--haze) 58%,
      var(--forest) 72%,
      var(--forest-dark) 86%,
      var(--road) 100%);
  }

  /* Front */
  .headline {
    position: absolute;
    left: 0; right: 0;
    text-align: center;
    color: var(--welcome-green);
    margin: 0;
    line-height: 1;
  }
  .headline-youre  { top: 50px;  font: 400 104px/1 "Federo", sans-serif; left: 12px; }
  .headline-warmly { top: 160px; font: 400 104px/1 "Federo", sans-serif; left: 28px; }
  .headline-welcome {
    top: 262px;
    font: 400 100px/1 "Bodoni Moda", serif;
    letter-spacing: -2px;
    left: 110px;
    right: auto;
    width: 530px;
    transform: scaleX(1.02);
  }
  .flourish {
    position: absolute;
    left: 146px; top: 390px;
    width: 420px; height: 72px;
    border-radius: 50%;
    background: radial-gradient(ellipse at center, rgba(140,207,63,0.45) 0%, rgba(140,207,63,0) 70%);
  }

  /* Back */
  .invite {
    position: absolute;
    left: 0; right: 0; top: 52px;
    text-align: center;
    color: var(--ink);
    font: 300 25px/38px "Comfortaa", sans-serif;
    margin: 0;
  }
  .invite strong { font-weight: 500; }
  .invite .special-guest {
    color: var(--guest-red);
    font: 400 36px/38px "Encode Sans Condensed", sans-serif;
  }
  .invite .venue { font-weight: 400; letter-spacing: -0.5px; }

  .contact {
    position: absolute;
    left: 70px; width: 430px; top: 420px;
    text-align: center;
    color: var(--paper);
    font: 400 16px/24px "Comfortaa", sans-serif;
    margin: 0;
  }

  .corner-panel {
    position: absolute;
    right: 0; bottom: 0;
    width: 728px; height: 527px;
  }
  .ministry-mark {
    position: absolute;
    left: 580px; top: 425px;
    width: 128px;
    text-align: center;
    font-family: "Comfortaa", sans-serif;
    font-weight: 500;
    color: var(--logo-red);
  }
  .ministry-mark .mark-dot {
    display: block;
    width: 28px; height: 28px;
    margin: 0 auto 5px;
    border-radius: 50%;
    background: var(--edge-blue);
  }
  .ministry-mark .mark-name { font-size: 8px; line-height: 9px; letter-spacing: 0.3px; }
  .ministry-mark .mark-tagline { font-size: 3.5px; line-height: 4px; margin-top: 2px; }
</style>
</head>
<body>

<section class="flyer-card flyer-front">
  <div class="scenery" role="img" aria-label="Photo of a misty road winding through autumn pine forest"></div>
  <h1 class="headline headline-youre">you’re</h1>
  <p class="headline headline-warmly">warmly</p>
  <p class="headline headline-welcome">WELCOME</p>
  <div class="flourish" role="img" aria-label="Green decorative scroll flourish"></div>
</section>

<section class="flyer-card flyer-back">
  <div class="scenery" role="img" aria-label="Photo of a misty road winding through autumn pine forest"></div>

  <p class="invite">
    We would love to have you<br>
    join us as our <span class="special-guest">SPECIAL GUEST</span><br>
    this <strong>Sunday at 10am.</strong><br>
    You can find us at<br>
    <span class="venue">Harvest Lantern Family Church,</span><br>
    <span class="venue">17-19 Marlow Crest Road</span><br>
    <span class="venue">(Behind Brivo), Thornbury Meadow Village, QX4 7LB</span>
  </p>

  <p class="contact">
    For more information or for a chat, please call us on<br>
    07700 900418 / 07700 900752 or<br>
    email church@hlfcuk-mail.test
  </p>

  <svg class="corner-panel" viewBox="0 0 728 527" aria-hidden="true">
    <path d="M530 527 C548 420 610 358 728 352 L728 527 Z" fill="var(--paper)"/>
    <path d="M530 527 C548 420 610 358 728 352" fill="none" stroke="var(--edge-blue)" stroke-width="3"/>
  </svg>

  <div class="ministry-mark">
    <span class="mark-dot"></span>
    <div class="mark-name">HARVEST LANTERN<br>MINISTRIES</div>
    <div class="mark-tagline">SHARING HOPE, SERVING THE VILLAGE<br>AND WALKING TOGETHER IN FAITH.</div>
  </div>
</section>

</body>
</html>
```